Zielgruppe
Die TORVEL GMBH steht Gewerbe- und Industriekunden in verschiedensten Bereichen zur Seite. Zielsetzung unserer Ingenieur- und Energiedienstleistungen ist eine niedrigere Energiekostenbelastung, eine Subventionsmaximierung für Ihre geplanten und zukünftigen Investitionen/Projekte und die nachhaltige Nutzung regenerativer Quellen zur Eigenversorgung mit Energie und Senkung des CO2-Ausstoßes!
Aufgabenstellung
Grundlegende Überschrift über den Flyer sollte sein: Energiekosten halbieren - mit unserem 4-Säulen Programm. Diese 4 Säulen sind:
Die vier zentralen Komponenten sind:
Energieaudit gemäß DIN 16247-1 : Dieses Audit, das durch das Norlander Zentralstelle Gewerbe gefördert wird, beinhaltet eine anschließende detaillierte Inspektion der Betriebsstätte durch einen qualifizierten Ingenieur, der die Energiebräuche analysiert und einen umfassenden Bericht erstellt. Dieser zeigt auf, wie das Unternehmen auch ohne Investitionen Energie sparen kann, wobei die aktuelle durchschnittliche Einsparung bei 21 % liegt. Unsere Ingenieure sind alle KLMU-zertifiziert und arbeiten exklusiv für uns.
Beantragung von Fördergeldern : Falls das Unternehmen Investitionen plant, stehen derzeit über 8000 Förderprogramme zur Verfügung. Wir übernehmen die Prüfung und Beantragung dieses Programms für das Unternehmen. Die Fördersummen variieren, betragen im Durchschnitt jedoch 41 %.
Steueroptimierung der Energierechnung : Produzierende Unternehmen können nach Antragstellung eine Rückerstattung von 2,05 Cent pro kWh auf ihre Energierechnung erhalten. Außerdem lässt sich die Konzessionsabgabe von durchschnittlich 1,80 Cent auf 0,11 Cent senken. Diese beiden Faktoren machen in der Regel 30 % des reinen Energiepreises aus.
Verbesserung der Strom- und Gasrechnung : Durch eine Ausschreibung auf nationaler Ebene können durchschnittlich 23 % der aktuellen Energiekosten reduziert werden.

```html
<!DOCTYPE html>
<html lang="de">
<head>
<meta charset="utf-8">
<title>Energiekosten halbieren – Flyer</title>
<link href="https://fonts.googleapis.com/css2?family=Oswald:wght@500;700&family=Open+Sans:ital,wght@0,300;0,400;0,700;1,300;1,700&display=swap" rel="stylesheet">
<style>
  :root{
    --bg:#e4e4e4;
    --paper:#ffffff;
    --forest-dark:#2f4424;
    --forest:#3f5a2e;
    --band:#55703f;
    --lime:#86c23a;
    --lime-soft:#c9e89a;
    --ink:#3a3a3c;
    --text:#333;
  }
  *{margin:0;padding:0;box-sizing:border-box}
  html,body{width:837px;height:1200px;overflow:hidden;background:var(--bg)}
  body{position:relative;font-family:"Open Sans",Arial,sans-serif;color:var(--text)}
  .page{position:absolute;top:330px;width:382px;height:539px;background:var(--paper);overflow:hidden;box-shadow:0 2px 8px rgba(0,0,0,.12)}
  .page--front{left:15px}
  .page--back{left:440px}
  .abs{position:absolute}
  .display{font-family:"Oswald",Impact,sans-serif;font-weight:700;text-transform:uppercase;letter-spacing:-.3px}

  /* front */
  .hero-photo{left:0;top:0;width:382px;height:370px;
    background:radial-gradient(circle at 78% 22%, #a7c77a 0, #8fb260 22%, transparent 45%),
               linear-gradient(180deg,#a9c98a 0%,#8fb06a 40%,#4e6a36 62%,var(--forest) 100%)}
  .front-title{left:14px;top:28px;color:#fff;font-size:28px;line-height:34px}
  .front-sub{left:14px;top:100px;color:#fff;font-style:italic;font-weight:300;font-size:13.5px;line-height:19px}
  .front-sub b{font-weight:700}
  .pillar{top:153px;width:108px;height:134px;background:linear-gradient(180deg,#fff 0%,#eef7df 35%,var(--lime-soft) 65%,var(--lime) 100%);text-align:center;padding:18px 6px 0}
  .pillar h3{font-family:"Oswald",Impact,sans-serif;font-weight:700;color:var(--ink);font-size:11.5px;line-height:15px}
  .pillar p{font-weight:300;font-size:7.8px;line-height:10.6px;margin-top:18px;color:#333}
  .about-h,.contact-h{top:376px;font-size:27px;line-height:32px;color:var(--ink)}
  .about-h{left:14px}
  .contact-h{left:260px}
  .about-text{left:14px;top:420px;width:212px;font-size:6.6px;line-height:9.3px;text-align:justify}
  .about-text p+p{margin-top:7px}
  .divider{left:244px;top:378px;width:1.2px;height:122px;background:var(--lime)}
  .contact-text{left:260px;top:420px;font-size:6.8px;line-height:9.3px}
  .contact-text b{font-style:italic}
  .bottom-glow{left:0;bottom:0;width:382px;height:70px;background:linear-gradient(180deg,rgba(134,194,58,0) 0%,rgba(134,194,58,.35) 60%,var(--lime) 100%)}
  .brand-name{font-family:"Open Sans",Arial,sans-serif;font-size:9px;font-weight:700;color:var(--ink)}
  .front-brand{left:14px;top:505px}

  /* back */
  .forest-photo{left:0;top:0;width:382px;height:210px;background:linear-gradient(180deg,#3a5229 0%,#31472a 55%,#2c4122 100%)}
  .back-kicker{left:26px;top:30px;color:#fff;font-style:italic;font-weight:300;font-size:13.5px}
  .back-title{left:26px;top:50px;color:#fff;font-size:28px;line-height:34px}
  .back-tag{left:26px;top:125px;color:#fff;font-style:italic;font-weight:300;font-size:13.5px;line-height:19.5px}
  .pillar-list{left:22px;width:350px}
  .step{position:absolute;left:0;width:350px}
  .step-num{position:absolute;left:0;top:-2px;font-family:"Oswald",Impact,sans-serif;font-weight:700;font-size:29px;line-height:30px;color:var(--ink)}
  .step h4{position:absolute;left:20px;top:0;font-family:"Oswald",Impact,sans-serif;font-weight:700;font-size:9.2px;color:var(--ink);white-space:nowrap}
  .step ul{position:absolute;left:20px;top:14px;list-style:none}
  .step li{font-size:6.8px;line-height:12px;font-weight:300;white-space:nowrap;display:flex;align-items:center;gap:4px;color:#333}
  .step li.cont{padding-left:11px;line-height:9px;margin-top:-3px}
  .tick{width:7px;height:7px;flex:none}
  .back-brand{left:26px;top:498px}
</style>
</head>
<body>

<section class="page page--front" aria-label="Flyer Vorderseite">
  <div class="abs hero-photo" role="img" aria-label="Unscharfes grünes Naturfoto mit einer moosbewachsenen Glühbirne"></div>
  <svg class="abs" style="left:0;top:0" width="382" height="539" viewBox="0 0 382 539" aria-hidden="true">
    <polygon points="0,235 382,235 382,314 0,363" fill="var(--forest)" opacity=".9"/>
    <polygon points="0,352 382,305 382,314 0,363" fill="var(--band)"/>
    <polygon points="0,363 382,314 382,539 0,539" fill="var(--paper)"/>
  </svg>
  <h1 class="abs display front-title">Energiekosten<br>halbieren –</h1>
  <p class="abs front-sub">mit unserem<br><b>4-Säulen-Programm!</b></p>

  <div class="abs pillar" style="left:14px"><h3>Individuelle<br>Energieanalysen</h3><p>Identifikation von Einsparpotenzialen und Optimierungsmöglichkei­ten.</p></div>
  <div class="abs pillar" style="left:137px"><h3>Fördermittel-<br>beratung</h3><p>Erschließung und Beantragung von staat­lichen Zuschüssen und Programmen.</p></div>
  <div class="abs pillar" style="left:260px"><h3>Energie- &amp; Steuer-<br>optimierung</h3><p>Reduzierung von Energiekosten durch gezielte Maßnahmen.</p></div>

  <div class="abs bottom-glow"></div>

  <h2 class="abs display about-h">Über uns</h2>
  <div class="abs about-text">
    <p>Die TORVEL GmbH ist Ihr erfahrener Partner für Energieeffizienz, Fördermittelmanagement und nachhaltige Versorgungskonzepte. Wir unterstützen Industrie- und Gewerbekunden deutschlandweit, Betriebskosten zu senken und gleichzeitig den CO₂-Ausstoß zu reduzieren.</p>
    <p>Durch unsere langjährige Erfahrung, eigene KLMU-zertifizierte Ingenieure und ein starkes Partnernetzwerk sind wir in der Lage, Ihnen maßgeschneiderte Lösungen anzubieten.</p>
  </div>
  <div class="abs divider"></div>
  <h2 class="abs display contact-h">Kontakt</h2>
  <address class="abs contact-text" style="font-style:normal">
    <b>TORVEL GmbH</b><br>Ahornweg 12<br>69412 Lindenau<br><br>Telefon: 06207 4418230<br>Mail: info@torvel-beispiel.de
  </address>
  <p class="abs brand-name front-brand">Torvel GmbH</p>
</section>

<section class="page page--back" aria-label="Flyer Rückseite">
  <div class="abs forest-photo" role="img" aria-label="Dunkelgrünes Waldfoto"></div>
  <svg class="abs" style="left:0;top:0" width="382" height="539" viewBox="0 0 382 539" aria-hidden="true">
    <defs><linearGradient id="glow" x1="0" y1="0" x2="0" y2="1"><stop offset="0" stop-color="#86c23a" stop-opacity="0"/><stop offset=".6" stop-color="#86c23a" stop-opacity=".35"/><stop offset="1" stop-color="#86c23a"/></linearGradient></defs>
    <polygon points="0,180 382,150 382,166 0,196" fill="var(--forest-dark)"/>
    <polygon points="0,196 382,166 382,182 0,207" fill="var(--band)"/>
    <polygon points="0,207 382,182 382,539 0,539" fill="var(--paper)"/>
    <rect x="0" y="469" width="382" height="70" fill="url(#glow)"/>
  </svg>
  <p class="abs back-kicker">Unser</p>
  <h1 class="abs display back-title">4-Säulen<br>Programm</h1>
  <p class="abs back-tag">setzt genau dort an, wo Unternehmen<br>am meisten sparen können!</p>

  <div class="abs pillar-list" style="top:0">
    <div class="step" style="top:223px">
      <span class="step-num">1</span>
      <h4>Energieaudit nach DIN 16247-1</h4>
      <ul>
        <li><svg class="tick" viewBox="0 0 8 8"><rect x=".5" y=".5" width="7" height="7" fill="none" stroke="#555" stroke-width=".8"/><path d="M1.8 4.2 3.4 5.8 6.4 2" fill="none" stroke="var(--lime)" stroke-width="1.2"/></svg>Durchführung durch eigene, KLMU-zertifizierte Ingenieure</li>
        <li><svg class="tick" viewBox="0 0 8 8"><rect x=".5" y=".5" width="7" height="7" fill="none" stroke="#555" stroke-width=".8"/><path d="M1.8 4.2 3.4 5.8 6.4 2" fill="none" stroke="var(--lime)" stroke-width="1.2"/></svg>Betriebsbegehung und ausführlicher Abschlussbericht (60–70 Seiten)</li>
        <li><svg class="tick" viewBox="0 0 8 8"><rect x=".5" y=".5" width="7" height="7" fill="none" stroke="#555" stroke-width=".8"/><path d="M1.8 4.2 3.4 5.8 6.4 2" fill="none" stroke="var(--lime)" stroke-width="1.2"/></svg>Konkrete Handlungsempfehlungen – ohne und mit Investitionen</li>
        <li class="cont">50 % Förderung durch das Norlander Zentralstelle Gewerbe (KLMU)</li>
      </ul>
    </div>
    <div class="step" style="top:292px">
      <span class="step-num">2</span>
      <h4>Fördergelder beantragen</h4>
      <ul>
        <li><svg class="tick" viewBox="0 0 8 8"><rect x=".5" y=".5" width="7" height="7" fill="none" stroke="#555" stroke-width=".8"/><path d="M1.8 4.2 3.4 5.8 6.4 2" fill="none" stroke="var(--lime)" stroke-width="1.2"/></svg>Zugang zu über 8.000 aktuellen Förderprogrammen</li>
        <li><svg class="tick" viewBox="0 0 8 8"><rect x=".5" y=".5" width="7" height="7" fill="none" stroke="#555" stroke-width=".8"/><path d="M1.8 4.2 3.4 5.8 6.4 2" fill="none" stroke="var(--lime)" stroke-width="1.2"/></svg>Prüfung und komplette Abwicklung der Anträge</li>
        <li><svg class="tick" viewBox="0 0 8 8"><rect x=".5" y=".5" width="7" height="7" fill="none" stroke="#555" stroke-width=".8"/><path d="M1.8 4.2 3.4 5.8 6.4 2" fill="none" stroke="var(--lime)" stroke-width="1.2"/></svg>Maximale Subventionsausnutzung für Ihre Investitionen und Projekte</li>
      </ul>
    </div>
    <div class="step" style="top:355px">
      <span class="step-num">3</span>
      <h4>Steueroptimierung Ihrer Energierechnung</h4>
      <ul>
        <li><svg class="tick" viewBox="0 0 8 8"><rect x=".5" y=".5" width="7" height="7" fill="none" stroke="#555" stroke-width=".8"/><path d="M1.8 4.2 3.4 5.8 6.4 2" fill="none" stroke="var(--lime)" stroke-width="1.2"/></svg>2,05 Cent pro kWh Rückerstattung für produzierende Unternehmen</li>
        <li><svg class="tick" viewBox="0 0 8 8"><rect x=".5" y=".5" width="7" height="7" fill="none" stroke="#555" stroke-width=".8"/><path d="M1.8 4.2 3.4 5.8 6.4 2" fill="none" stroke="var(--lime)" stroke-width="1.2"/></svg>Konzessionsabgabe-Senkung: Von Ø 1,80 Cent auf nur 0,11 Cent</li>
        <li><svg class="tick" viewBox="0 0 8 8"><rect x=".5" y=".5" width="7" height="7" fill="none" stroke="#555" stroke-width=".8"/><path d="M1.8 4.2 3.4 5.8 6.4 2" fill="none" stroke="var(--lime)" stroke-width="1.2"/></svg>Bis zu 50 % Ersparnis allein beim Energiepreis möglich!</li>
      </ul>
    </div>
    <div class="step" style="top:419px">
      <span class="step-num">4</span>
      <h4>Optimierung der Strom- und Gasbezugskosten</h4>
      <ul>
        <li><svg class="tick" viewBox="0 0 8 8"><rect x=".5" y=".5" width="7" height="7" fill="none" stroke="#555" stroke-width=".8"/><path d="M1.8 4.2 3.4 5.8 6.4 2" fill="none" stroke="var(--lime)" stroke-width="1.2"/></svg>Durchführung bundesweiter Ausschreibungen</li>
        <li><svg class="tick" viewBox="0 0 8 8"><rect x=".5" y=".5" width="7" height="7" fill="none" stroke="#555" stroke-width=".8"/><path d="M1.8 4.2 3.4 5.8 6.4 2" fill="none" stroke="var(--lime)" stroke-width="1.2"/></svg>Durchschnittlich 21 % Einsparung auf Ihre aktuellen EnergiekostenCent</li>
      </ul>
    </div>
  </div>
  <p class="abs brand-name back-brand">Torvel GmbH</p>
</section>

</body>
</html>
```